Business Card- Occupational Therapist

I need business cards for Bright Harbour KidMotion, I am an Occupational Therapist offering child centred play therapy.
I am a sole private practitioner offering play therapy services to families in rural Great Southern region of WA, my mission statement is "helping rural children and communities thrive"
This is a new business so I am needing to promote the value of child centred play therapy within the community, and my referrers (target audience) will be: rural GPs (doctors), child health nurse, schools, disability providers, child protection workers etc) but also the families of young children in rural areas.
Target Market(s)
Families of children
Referrers (Doctors, child health nurse, schools, disability providers, child protection workers)
Industry/Entity Type
Mental Health
Contact Information for Business Card
Maren Koltwick
Occupational Therapist
Phone: 0471 828 305
Email: maren@bhkidmotion.com.au
PO Box 71 | TARRALEIGH WA 6412
Requirements
Must have
- Include Bright Harbour KidMotion logo and my contact details.
Include my credentials as an Occupational Therapist and Child Centred Play Therapist
Nice to have
- "Play is a child's language and toys are their words" Dorian Welkmore

```html
<!DOCTYPE html>
<html lang="en">
<head>
<meta charset="utf-8">
<title>Bright Harbour KidMotion – Business Card</title>
<link rel="stylesheet" href="https://fonts.googleapis.com/css2?family=Quicksand:wght@500&family=Arimo:wght@400;700&display=swap">
<style>
  :root {
    --canvas: #c9c9c9;
    --card-white: #ffffff;
    --brand-green: #23a94b;
    --brand-purple: #6b2474;
    --ink: #2b2b2b;
  }
  * { box-sizing: border-box; margin: 0; padding: 0; }
  html, body { width: 1200px; height: 788px; overflow: hidden; }
  body {
    background: var(--canvas);
    display: flex;
    align-items: center;
    justify-content: center;
    gap: 40px;
  }
  .card {
    position: relative;
    width: 540px;
    height: 309px;
    border-radius: 22px;
    overflow: hidden;
    box-shadow: 0 10px 24px rgba(0,0,0,0.22);
  }
  .card--front { background: var(--card-white); }
  .card--back {
    background: var(--brand-green);
    display: flex;
    align-items: center;
    justify-content: center;
  }
  .front-wave { position: absolute; inset: 0; width: 100%; height: 100%; }

  .brand {
    display: flex;
    align-items: center;
    gap: 10px;
    font-family: "Quicksand", sans-serif;
    font-weight: 500;
    line-height: 1.05;
  }
  .brand__dot { border-radius: 50%; flex: none; }
  .brand--front {
    position: absolute;
    left: 34px;
    top: 92px;
    color: var(--ink);
    font-size: 21px;
  }
  .brand--front .brand__dot { width: 34px; height: 34px; background: var(--brand-green); }
  .brand--back {
    flex-direction: column;
    color: var(--card-white);
    font-size: 36px;
    text-align: center;
    gap: 22px;
  }
  .brand--back .brand__dot { width: 110px; height: 110px; background: var(--card-white); }

  .divider {
    position: absolute;
    left: 248px;
    top: 72px;
    width: 1.5px;
    height: 100px;
    background: var(--brand-purple);
  }
  .contact {
    position: absolute;
    left: 266px;
    top: 36px;
    font-family: "Arimo", sans-serif;
    color: var(--ink);
  }
  .contact__name {
    font-size: 22px;
    font-weight: 700;
    letter-spacing: 0.5px;
    line-height: 1.15;
  }
  .contact__first { color: var(--brand-green); }
  .contact__last { color: var(--brand-purple); }
  .contact__title { font-size: 13px; margin-top: 2px; }
  .contact__list { list-style: none; margin-top: 12px; font-size: 12.5px; }
  .contact__list li { display: flex; align-items: center; gap: 8px; margin-bottom: 5px; white-space: nowrap; }
  .contact__icon { width: 12px; height: 12px; fill: var(--brand-green); flex: none; }
</style>
</head>
<body>
  <section class="card card--front" aria-label="Card front">
    <svg class="front-wave" viewBox="0 0 540 309" preserveAspectRatio="none" aria-hidden="true">
      <path d="M0,292 C300,290 470,240 540,156 L540,309 L0,309 Z" fill="var(--brand-purple)"/>
      <path d="M0,297 C302,295 474,248 540,166 L540,309 L0,309 Z" fill="var(--card-white)"/>
      <path d="M0,300 C304,298 476,253 540,172 L540,309 L0,309 Z" fill="var(--brand-green)"/>
    </svg>

    <div class="brand brand--front">
      <span class="brand__dot"></span>
      <span class="brand__name">Bright Harbour<br>KidMotion</span>
    </div>

    <div class="divider"></div>

    <div class="contact">
      <h1 class="contact__name"><span class="contact__first">MAREN</span> <span class="contact__last">KOLTWICK</span></h1>
      <p class="contact__title">Occupational Therapist</p>
      <ul class="contact__list">
        <li>
          <svg class="contact__icon" viewBox="0 0 24 24" aria-hidden="true"><path d="M6.6 10.8a15 15 0 0 0 6.6 6.6l2.2-2.2c.3-.3.7-.4 1-.2 1.1.4 2.3.6 3.6.6.6 0 1 .4 1 1V20c0 .6-.4 1-1 1A17 17 0 0 1 3 4c0-.6.4-1 1-1h3.5c.6 0 1 .4 1 1 0 1.3.2 2.5.6 3.6.1.3 0 .7-.2 1z"/></svg>
          0471 828 305
        </li>
        <li>
          <svg class="contact__icon" viewBox="0 0 24 24" aria-hidden="true"><path d="M2 5h20v14H2z M2 5l10 8 10-8" stroke="#fff" stroke-width="1.5"/></svg>
          maren@bhkidmotion.com.au
        </li>
        <li>
          <svg class="contact__icon" viewBox="0 0 24 24" aria-hidden="true"><path d="M12 2a7 7 0 0 0-7 7c0 5 7 13 7 13s7-8 7-13a7 7 0 0 0-7-7zm0 9.5A2.5 2.5 0 1 1 12 6.5a2.5 2.5 0 0 1 0 5z"/></svg>
          PO Box 71 | TARRALEIGH WA 6412
        </li>
      </ul>
    </div>
  </section>

  <section class="card card--back" aria-label="Card back">
    <div class="brand brand--back">
      <span class="brand__name">Bright Harbour<br>KidMotion</span>
      <span class="brand__dot"></span>
    </div>
  </section>
</body>
</html>
```